Web design for TRADEBACKS. A forex rebate platform website

I need a complete design for a forex rebate website called TRADEBACKS. The website will include the following pages:

- Homepage
- Broker Listing Page
- Broker Rebate Detail Page

Please review the attached file for detailed requirements and the content that needs to be designed.

Number of Pages Required

3 page

```html
<!DOCTYPE html>
<html lang="en">
<head>
<meta charset="utf-8">
<title>TRADEBACKS – Forex Rebates Made Simple</title>
<link href="https://fonts.googleapis.com/css2?family=Inter:wght@400;500;600;700&family=Plus+Jakarta+Sans:wght@600;700;800&display=swap" rel="stylesheet">
<style>
:root{
  --bg:#0b1a40;
  --band:#0e1f4d;
  --card:#112457;
  --card-2:#0f2151;
  --line:#1f3672;
  --text:#ffffff;
  --muted:#8f9fc6;
  --soft:#b9c5e3;
  --blue:#1f6bff;
  --blue-2:#3d84ff;
  --green:#22d39a;
  --orange:#ff7a1a;
  --red:#e8432f;
  --gold:#ffc23d;
  --badge:#1f3f8c;
}
*{box-sizing:border-box;margin:0;padding:0}
html,body{width:1200px;height:4307px;overflow:hidden}
body{background:var(--bg);color:var(--text);font-family:"Inter",sans-serif;font-size:10px;line-height:1.5}
h1,h2,h3,.display{font-family:"Plus Jakarta Sans",sans-serif}
.wrap{width:725px;margin:0 auto;position:relative}
section{position:relative}
.band{position:absolute;left:200px;width:800px;background:var(--band);border-top:1px solid #17306a;border-bottom:1px solid #17306a}
.eyebrow{font-size:7px;font-weight:700;letter-spacing:1.2px;color:var(--blue-2);text-transform:uppercase}
.sec-title{font-size:23px;font-weight:800;letter-spacing:-.4px;line-height:1.2}
.sec-lead{font-size:10.5px;color:var(--muted);line-height:1.7}
.center{text-align:center}
.btn{display:inline-flex;align-items:center;justify-content:center;height:28px;padding:0 18px;border-radius:4px;font-size:9.5px;font-weight:600}
.btn-primary{background:var(--blue);color:#fff}
.btn-ghost{border:1px solid var(--line);color:var(--soft)}

/* nav */
.nav{height:42px;border-bottom:1px solid #16306a;display:flex;align-items:center;padding:0 25px;position:relative}
.logo{display:flex;align-items:center;gap:6px;font-family:"Plus Jakarta Sans",sans-serif;font-weight:800;font-size:15px;color:#fff}
.logo-dot{width:9px;height:9px;background:var(--blue);border-radius:2px}
.nav-links{position:absolute;left:456px;display:flex;gap:22px;font-size:9px;color:var(--soft)}
.nav-right{margin-left:auto;display:flex;align-items:center;gap:10px;font-size:9px}
.lang{height:20px;padding:0 8px;border:1px solid var(--line);border-radius:10px;display:flex;align-items:center;gap:4px;color:var(--soft)}
.lang i{width:7px;height:7px;border-radius:50%;background:var(--blue-2)}
.login{height:20px;padding:0 10px;border:1px solid var(--line);border-radius:4px;display:flex;align-items:center;color:var(--blue-2)}
.signup{height:20px;padding:0 14px;border-radius:4px;background:var(--blue);display:flex;align-items:center;font-weight:600}

/* hero */
.hero{height:434px}
.hero-copy{position:absolute;left:0;top:50px;width:350px}
.live-pill{display:inline-flex;align-items:center;gap:5px;height:17px;padding:0 9px;border:1px solid #24418a;background:#10245a;border-radius:9px;font-size:7px;font-weight:700;color:var(--blue-2);letter-spacing:.6px}
.live-pill i{width:5px;height:5px;border-radius:50%;background:var(--blue-2)}
.hero h1{margin-top:17px;font-size:36px;line-height:1.05;font-weight:800;letter-spacing:-.8px}
.hero h1 span{color:var(--blue)}
.hero p{margin-top:18px;font-size:10.5px;color:var(--soft);line-height:1.75;width:300px}
.hero-cta{margin-top:19px;display:flex;gap:10px}
.hero-cta .btn-primary{width:146px}
.hero-rule{margin-top:29px;height:1px;background:var(--line);width:346px}
.stats{margin-top:24px;display:flex;gap:21px}
.stat b{display:block;font-family:"Plus Jakarta Sans",sans-serif;font-size:14px;font-weight:800}
.stat span{font-size:7px;color:var(--muted)}

.dash{position:absolute;left:381px;top:47px;width:344px;height:352px;background:#102352;border:1px solid var(--line);border-radius:10px;padding:18px 16px}
.dash-head{display:flex;justify-content:space-between;align-items:center;font-size:7.5px;font-weight:700;letter-spacing:.8px;color:var(--soft)}
.live-tag{font-size:6.5px;color:var(--green);background:#123f4a;border-radius:8px;padding:2px 7px;letter-spacing:0}
.dash-label{margin-top:13px;font-size:7px;color:var(--muted)}
.dash-total{font-family:"Plus Jakarta Sans",sans-serif;font-size:24px;font-weight:800;margin-top:4px}
.dash-up{font-size:7px;color:var(--green);margin-top:2px}
.bars{margin-top:12px;height:52px;display:flex;align-items:flex-end;gap:3px}
.bars i{flex:1;background:#1c3a80;border-radius:1px}
.bars i.hi{background:var(--blue)}
.minis{margin-top:13px;display:grid;grid-template-columns:1fr 1fr;gap:7px}
.mini{height:54px;background:#0f2050;border:1px solid var(--line);border-radius:5px;padding:8px 9px}
.mini small{font-size:6.5px;color:var(--muted);display:block}
.mini b{font-size:11px;display:block;margin-top:2px}
.mini em{font-style:normal;font-size:6px;color:var(--green)}
.notice{margin-top:10px;height:22px;border:1px solid #1d4a5a;background:#0f2a4f;border-radius:5px;display:flex;align-items:center;gap:6px;padding:0 9px;font-size:7px;color:var(--soft)}
.notice i{width:5px;height:5px;border-radius:50%;background:var(--green)}
.notice b{color:var(--green);font-weight:600}

/* ticker */
.ticker{height:30px;border-top:1px solid #16306a;border-bottom:1px solid #16306a;background:#0a1839;overflow:hidden;white-space:nowrap}
.ticker-row{position:absolute;left:-14px;top:0;height:30px;display:flex;align-items:center;gap:28px;font-size:8px;color:var(--soft)}
.tick{display:flex;align-items:center;gap:6px}
.tick .flag{width:11px;height:8px;border-radius:1px;background:#c93d4f}
.tick b{color:var(--green);font-weight:700}
.tick .ago{color:var(--muted);margin-left:14px}

/* how */
.how{height:356px}
.how .band{top:4px;height:352px}
.how .inner{position:relative;padding-top:62px}
.how .sec-title{margin-top:9px}
.how .sec-lead{width:330px;margin:8px auto 0;font-size:10px}
.cycle{margin-top:38px;display:flex;justify-content:center;align-items:flex-start;gap:14px}
.cycle-step{width:120px;text-align:center}
.cycle-icon{width:36px;height:36px;margin:0 auto;border:1px solid #2a4a96;background:#13306e;border-radius:7px;display:flex;align-items:center;justify-content:center}
.cycle-step h3{margin-top:12px;font-size:9px;font-weight:700}
.cycle-step p{margin-top:4px;font-size:7px;color:var(--muted);line-height:1.6}
.cycle-arrow{margin-top:26px;color:var(--blue-2);font-size:14px}

/* brokers */
.brokers{height:630px}
.brokers .inner{padding-top:62px}
.brokers .sec-title{margin-top:8px}
.brokers .sec-lead{margin-top:6px;width:330px;font-size:10px}
.broker-grid{margin-top:31px;display:grid;grid-template-columns:repeat(3,1fr);gap:21px 10px}
.broker{height:162px;background:var(--card-2);border:1px solid var(--line);border-radius:7px;padding:15px 15px}
.broker:nth-child(n+4){height:168px}
.broker-head{display:flex;align-items:center;gap:8px}
.badge{width:24px;height:24px;border-radius:5px;background:var(--badge);flex:none}
.broker-head b{font-size:9px;display:block}
.broker-head small{font-size:6.5px;color:var(--muted)}
.rate{margin-top:12px;font-family:"Plus Jakarta Sans",sans-serif;font-size:17px;font-weight:800;color:var(--blue)}
.rate span{font-size:8px;color:var(--soft);font-weight:600}
.rate-note{font-size:7px;color:var(--muted)}
.tags{margin-top:10px;display:flex;gap:5px}
.tags span{font-size:6px;color:var(--soft);border:1px solid var(--line);border-radius:8px;padding:2px 7px}
.view{margin-top:14px;height:20px;border:1px solid #27469a;border-radius:4px;display:flex;align-items:center;justify-content:center;font-size:7px;color:var(--blue-2);gap:8px}
.view-all{margin:35px auto 0;width:138px;height:24px;border:1px solid #27469a;border-radius:4px;display:flex;align-items:center;justify-content:center;gap:6px;font-size:8px;color:var(--blue-2)}

/* calculator */
.calc{height:415px}
.calc .band{top:0;height:415px}
.calc-copy{position:absolute;left:0;top:90px;width:346px}
.calc-copy .sec-title{margin-top:7px;font-size:22px;line-height:1.22}
.calc-copy .sec-lead{margin-top:9px;font-size:10px}
.feature{margin-top:12px;height:42px;border:1px solid var(--line);background:#102352;border-radius:5px;display:flex;align-items:center;gap:12px;padding:0 13px}
.feature:first-of-type{margin-top:16px}
.feature b{font-size:8px;display:block}
.feature small{font-size:6.5px;color:var(--muted)}
.calc-card{position:absolute;left:381px;top:54px;width:344px;height:300px;background:#102352;border:1px solid var(--line);border-radius:9px;padding:19px 20px}
.row-lbl{display:flex;justify-content:space-between;font-size:7px;color:var(--muted)}
.select{margin-top:9px;height:26px;border:1px solid #2a4786;background:#0d1e4b;border-radius:4px;display:flex;align-items:center;padding:0 11px;font-size:8.5px}
.slider{margin-top:10px;height:3px;background:#1e3a7e;border-radius:2px;position:relative}
.slider i{position:absolute;left:0;top:0;height:3px;background:var(--blue);border-radius:2px}
.slider b{position:absolute;top:-4px;width:11px;height:11px;border-radius:50%;background:#fff;border:2px solid var(--blue)}
.result{margin-top:34px;height:85px;border:1px solid #2a4786;background:#0d1e4b;border-radius:6px;padding:16px 14px}
.result-row{display:flex;justify-content:space-between;align-items:center;font-size:7.5px;color:var(--muted)}
.result-row b{font-family:"Plus Jakarta Sans",sans-serif;color:var(--green);font-size:14px}
.result-row + .result-row{margin-top:12px}
.result-row + .result-row b{font-size:19px}

/* why */
.why{height:332px}
.why .inner{padding-top:62px}
.why .sec-title{margin-top:6px}
.why-grid{margin-top:27px;display:grid;grid-template-columns:repeat(4,1fr);gap:13px}
.why-card{height:135px;background:#102352;border:1px solid var(--line);border-radius:7px;padding:18px 16px}
.ico{width:26px;height:26px;border-radius:5px;background:#163478;display:flex;align-items:center;justify-content:center}
.why-card h3{margin-top:13px;font-size:8.5px;font-weight:700}
.why-card p{margin-top:4px;font-size:7.2px;color:var(--muted);line-height:1.65}

/* steps */
.steps{height:418px}
.steps .band{top:0;height:418px;background:#0c1c48;border:none}
.steps .inner{padding-top:61px}
.steps .sec-title{margin-top:6px}
.steps .sec-lead{margin:6px auto 0;width:330px;font-size:10px}
.step-grid{margin-top:31px;display:grid;grid-template-columns:243px 222px 231px;gap:14px}
.step{height:150px;background:#102352;border:1px solid var(--line);border-radius:8px;padding:18px 20px;position:relative;overflow:hidden}
.step .num{position:absolute;right:14px;top:8px;font-family:"Plus Jakarta Sans",sans-serif;font-size:40px;font-weight:800;color:#16306b}
.step .ico{width:30px;height:30px;background:var(--blue)}
.step h3{margin-top:14px;font-size:9.5px;font-weight:700}
.step p{margin-top:6px;font-size:7.5px;color:var(--muted);line-height:1.7}

/* proof */
.proof{height:638px}
.proof .inner{padding-top:31px}
.proof .sec-title{margin-top:6px}
.proof .sec-lead{margin-top:5px;width:300px;font-size:10px}
.quotes{position:absolute;left:0;top:145px;width:350px}
.quote{background:#102352;border:1px solid var(--line);border-radius:7px;padding:15px 16px;margin-bottom:10px}
.quote:nth-child(1){height:136px}
.quote:nth-child(2){height:132px}
.quote:nth-child(3){height:146px}
.who{display:flex;align-items:center;gap:9px}
.avatar{width:24px;height:24px;border-radius:50%;display:flex;align-items:center;justify-content:center;font-size:8px;font-weight:700}
.who b{font-size:8.5px;display:block}
.who small{font-size:6.5px;color:var(--muted)}
.stars{margin-top:8px;color:var(--gold);font-size:8px;letter-spacing:1px}
.quote p{margin-top:6px;font-size:7.5px;color:var(--soft);line-height:1.65}
.earned{display:inline-block;margin-top:9px;font-size:6.5px;color:var(--green);background:#123f4a;border-radius:8px;padding:2px 8px}
.payouts{position:absolute;left:375px;top:150px;width:350px}
.pay-head{display:flex;align-items:center;gap:7px;font-size:7.5px;color:var(--soft)}
.pay-head span{font-size:6.5px;color:var(--green);background:#123f4a;border-radius:8px;padding:2px 7px}
.pay-grid{margin-top:12px;display:grid;grid-template-columns:160px 171px;gap:10px 18px}
.pay{height:75px;background:#102352;border:1px solid var(--line);border-radius:6px;padding:10px 11px;position:relative}
.pay small{font-size:6.5px;color:var(--muted);display:block}
.pay b{display:block;margin-top:8px;font-family:"Plus Jakarta Sans",sans-serif;font-size:15px}
.pay em{font-style:normal;font-size:6px;color:var(--muted);display:block;margin-top:6px}
.pay .new{position:absolute;right:9px;top:9px;font-size:5.5px;font-weight:700;background:var(--blue);border-radius:6px;padding:1px 6px}
.pay:nth-child(n+3){height:79px}
.methods{margin-top:18px;font-size:7px;letter-spacing:.7px;color:var(--soft);font-weight:600}
.chips{margin-top:9px;display:flex;gap:8px}
.chips span{height:21px;padding:0 9px;border:1px solid var(--line);background:#102352;border-radius:4px;display:flex;align-items:center;font-size:7px;color:var(--soft)}

/* faq */
.faq{height:448px}
.faq .inner{padding-top:63px}
.faq .sec-title{margin-top:9px}
.faq-list{width:450px;margin:36px auto 0}
.faq-q{display:flex;justify-content:space-between;font-size:8.5px;font-weight:700;padding-bottom:17px;border-bottom:1px solid #1a3069;margin-bottom:14px}
.faq-q span{color:var(--blue-2);font-weight:400}
.faq-open{border-bottom:1px solid #1a3069;padding-bottom:18px;margin-bottom:14px}
.faq-open .faq-q{border:none;padding-bottom:0;margin-bottom:12px}
.faq-open p{font-size:8px;color:var(--soft);line-height:1.8}

/* cta */
.cta{height:297px}
.cta .band{top:0;height:297px;background:linear-gradient(180deg,#0f2352,#0c1d48);border:none}
.cta .inner{padding-top:68px}
.cta h2{font-size:30px;font-weight:800;line-height:1.62;letter-spacing:-.5px}
.cta p{margin-top:8px;font-size:10.5px;color:var(--soft)}
.cta-btns{margin-top:16px;display:flex;justify-content:center;gap:9px}
.cta-btns .btn{height:29px}
.cta-btns .btn-primary{width:156px}

/* footer */
.footer{height:267px;border-top:1px solid #16306a;background:#091735}
.footer .inner{padding-top:44px;display:flex}
.f-brand{width:278px}
.f-brand p{margin-top:9px;font-size:8px;color:var(--muted);line-height:1.75;width:180px}
.socials{margin-top:12px;display:flex;gap:7px}
.socials i{width:21px;height:21px;border:1px solid var(--line);border-radius:50%}
.f-col{width:170px}
.f-col h4{font-size:7px;letter-spacing:1px;color:var(--soft)}
.f-col a{display:block;margin-top:9px;font-size:8px;color:var(--muted);text-decoration:none}
.f-bottom{position:absolute;left:0;top:152px;width:725px;display:flex;justify-content:space-between;font-size:7px;color:var(--muted)}
.f-bottom .disc{width:380px;font-size:6.3px;line-height:1.5}
</style>
</head>
<body>

<header class="nav">
  <div class="logo"><span class="logo-dot"></span>TRADEBACKS</div>
  <nav class="nav-links"><span>How It Works</span><span>Brokers</span><span>About</span><span>News</span></nav>
  <div class="nav-right">
    <span class="lang"><i></i>EN</span>
    <span class="login">Log in</span>
    <span class="signup">Sign Up Free</span>
  </div>
</header>

<section class="hero">
  <div class="wrap">
    <div class="hero-copy">
      <span class="live-pill"><i></i>LIVE PAYOUTS ACTIVE</span>
      <h1>Forex Rebates<br>Made Simple.<br><span>Up To 90% Back.</span></h1>
      <p>Earn higher rebates from the world's leading forex brokers without affecting your spreads, commissions, or trading conditions.</p>
      <div class="hero-cta">
        <span class="btn btn-primary">Start Earning Rebates</span>
        <span class="btn btn-ghost">Compare Brokers</span>
      </div>
      <div class="hero-rule"></div>
      <div class="stats">
        <div class="stat"><b>$7.5M+</b><span>Rebates Paid</span></div>
        <div class="stat"><b>15,000+</b><span>Active Traders</span></div>
        <div class="stat"><b>40+</b><span>Supported Brokers</span></div>
        <div class="stat"><b>Daily</b><span>Payout Frequency</span></div>
      </div>
    </div>

    <div class="dash">
      <div class="dash-head">REBATE DASHBOARD <span class="live-tag">● Live</span></div>
      <div class="dash-label">Total Earned This Month</div>
      <div class="dash-total">$2,847.50</div>
      <div class="dash-up">↑ +$412 from last month</div>
      <div class="bars">
        <i style="height:30%"></i><i style="height:45%"></i><i style="height:40%"></i><i style="height:55%"></i><i style="height:50%"></i><i style="height:45%"></i><i style="height:75%"></i><i class="hi" style="height:100%"></i>
      </div>
      <div class="minis">
        <div class="mini"><small>Northgate FX</small><b>$1,240</b><em>↑ $68d</em></div>
        <div class="mini"><small>Exvora</small><b>$890</b><em>↑ $64d</em></div>
        <div class="mini"><small>Peakline</small><b>$520</b><em>↑ $71d</em></div>
        <div class="mini"><small>Zenmark Group</small><b>$197</b><em>↑ $12d</em></div>
      </div>
      <div class="notice"><i></i>Arun (Thailand) received <b>$412.30</b> just now</div>
    </div>
  </div>
</section>

<section class="ticker">
  <div class="ticker-row">
    <span class="tick">nesia) received <b>$245.80</b> via USDT <span class="ago">2 min ago</span></span>
    <span class="tick"><span class="flag"></span>Niran (Thailand) received <b>$189.40</b> via Bank <span class="ago">4 min ago</span></span>
    <span class="tick"><span class="flag" style="background:#2a9c57"></span>Tunde (Nigeria) received <b>$376.20</b> via BTC <span class="ago">6 min ago</span></span>
    <span class="tick"><span class="flag"></span>Bao (Vietnam) received <b>$124.60</b> via USDT <span class="ago">9 min ago</span></span>
    <span class="tick"><span class="flag" style="background:#3b7d4e"></span>Pieter (South Africa) received <b>$302.10</b> via Bank</span>
  </div>
</section>

<section class="how">
  <div class="band"></div>
  <div class="wrap inner center">
    <div class="eyebrow">How It Works</div>
    <h2 class="sec-title">The Rebate Cycle, Explained</h2>
    <p class="sec-lead">Every trade you place generates spread or commission fees. Instead of those costs disappearing, TRADEBACKS returns a significant portion back to you automatically.</p>
    <div class="cycle">
      <div class="cycle-step">
        <div class="cycle-icon"><svg width="16" height="16" viewBox="0 0 16 16"><rect x="1" y="1" width="14" height="14" rx="2" fill="#fff"/><path d="M3 12l3-4 3 2 4-6" stroke="#e8432f" stroke-width="1.6" fill="none"/></svg></div>
        <h3>You Trade</h3>
        <p>Keep trading with your broker normally. No changes to spreads or execution.</p>
      </div>
      <div class="cycle-arrow">→</div>
      <div class="cycle-step">
        <div class="cycle-icon"><svg width="16" height="16" viewBox="0 0 16 16"><path d="M1 8l4-3h6l4 3-4 4H5z" fill="#ffc23d"/></svg></div>
        <h3>Broker Pays Us</h3>
        <p>Your broker pays TRADEBACKS a commission for introducing you as a client.</p>
      </div>
      <div class="cycle-arrow">→</div>
      <div class="cycle-step">
        <div class="cycle-icon"><svg width="16" height="16" viewBox="0 0 16 16"><circle cx="8" cy="9.5" r="5.5" fill="#ffc23d"/><path d="M6 2h4l-1 2H7z" fill="#ffc23d"/></svg></div>
        <h3>You Get Paid</h3>
        <p>We share up to $50 per lot back with you through daily rebate payments.</p>
      </div>
    </div>
  </div>
</section>

<section class="brokers">
  <div class="wrap inner">
    <div class="eyebrow">Partner Brokers</div>
    <h2 class="sec-title">40+ Trusted Broker Partnerships</h2>
    <p class="sec-lead">Top-rated brokers with the highest rebate rates. All verified, regulated, and ready to pay.</p>
    <div class="broker-grid">
      <article class="broker">
        <div class="broker-head"><span class="badge"></span><div><b>Northgate FX</b><small>ECN · Raw Spread</small></div></div>
        <div class="rate">$8.00<span>/lot</span></div><div class="rate-note">Max Rebate on Standard</div>
        <div class="tags"><span>ASIC</span><span>CySEC</span><span>FSA</span><span>TX4/TX5</span></div>
        <div class="view">View Rates &amp; Get Rebate <span>→</span></div>
      </article>
      <article class="broker">
        <div class="broker-head"><span class="badge"></span><div><b>Exvora</b><small>Market Maker · Low Spread</small></div></div>
        <div class="rate">$6.00<span>/lot</span></div><div class="rate-note">Max Rebate on Standard</div>
        <div class="tags"><span>FCA</span><span>CySEC</span><span>TX4/TX5</span></div>
        <div class="view">View Rates &amp; Get Rebate <span>→</span></div>
      </article>
      <article class="broker">
        <div class="broker-head"><span class="badge"></span><div><b>Peakline</b><small>ECN · cDesk</small></div></div>
        <div class="rate">$7.00<span>/lot</span></div><div class="rate-note">Max Rebate on Edge</div>
        <div class="tags"><span>ASIC</span><span>FCA</span><span>DFSA</span></div>
        <div class="view">View Rates &amp; Get Rebate <span>→</span></div>
      </article>
      <article class="broker">
        <div class="broker-head"><span class="badge"></span><div><b>Zenmark Group</b><small>STP · Micro Accounts</small></div></div>
        <div class="rate">$5.00<span>/lot</span></div><div class="rate-note">Max Rebate on Lite</div>
        <div class="tags"><span>CySEC</span><span>ASIC</span><span>TX4/TX5</span></div>
        <div class="view">View Rates &amp; Get Rebate <span>→</span></div>
      </article>
      <article class="broker">
        <div class="broker-head"><span class="badge"></span><div><b>Fairpoint Markets</b><small>ECN · Raw Spread</small></div></div>
        <div class="rate">$6.50<span>/lot</span></div><div class="rate-note">Max Rebate on Raw</div>
        <div class="tags"><span>ASIC</span><span>CySEC</span><span>cDesk</span></div>
        <div class="view">View Rates &amp; Get Rebate <span>→</span></div>
      </article>
      <article class="broker">
        <div class="broker-head"><span class="badge"></span><div><b>Vantora</b><small>ECN · Pro Accounts</small></div></div>
        <div class="rate">$7.50<span>/lot</span></div><div class="rate-note">Max Rebate on ECN</div>
        <div class="tags"><span>ASIC</span><span>FCA</span><span>TX4/TX5</span></div>
        <div class="view">View Rates &amp; Get Rebate <span>→</span></div>
      </article>
    </div>
    <div class="view-all">View All 40+ Brokers <span>→</span></div>
  </div>
</section>

<section class="calc">
  <div class="band"></div>
  <div class="wrap" style="height:415px">
    <div class="calc-copy">
      <div class="eyebrow">Rebate Calculator</div>
      <h2 class="sec-title">See What You've<br>Been Missing</h2>
      <p class="sec-lead">Select your broker and typical trading volume to instantly calculate your potential monthly and yearly rebate earnings.</p>
      <div class="feature"><svg width="12" height="14" viewBox="0 0 12 14"><path d="M7 0L1 8h4l-1 6 6-8H6z" fill="#ffc23d"/></svg><div><b>No impact on your trading</b><small>Spreads and conditions stay identical</small></div></div>
      <div class="feature"><svg width="13" height="13" viewBox="0 0 13 13"><rect x="0.5" y="1.5" width="12" height="11" rx="1.5" fill="#fff"/><rect x="0.5" y="1.5" width="12" height="3.5" fill="#e8432f"/></svg><div><b>Daily automatic payouts</b><small>Rebates credited to your account daily</small></div></div>
    </div>
    <div class="calc-card">
      <div class="row-lbl"><span>Select Broker</span><span>Northgate FX selected</span></div>
      <div class="select">Northgate FX – up to $8/lot</div>
      <div class="row-lbl" style="margin-top:16px"><span>Daily Lots Traded</span><span>10 lots/day</span></div>
      <div class="slider"><i style="width:6%"></i><b style="left:4%"></b></div>
      <div class="row-lbl" style="margin-top:26px"><span>Trading Days / Month</span><span>20 days</span></div>
      <div class="slider"><i style="width:74%"></i><b style="left:72%"></b></div>
      <div class="result">
        <div class="result-row"><span>Monthly Rebate</span><b>$1,600.00</b></div>
        <div class="result-row"><span>Yearly Rebate</span><b>$19,200.00</b></div>
      </div>
    </div>
  </div>
</section>

<section class="why">
  <div class="wrap inner center">
    <div class="eyebrow">Why TRADEBACKS</div>
    <h2 class="sec-title" style="font-size:21px">Built for Serious Traders</h2>
    <div class="why-grid" style="text-align:left">
      <div class="why-card"><div class="ico"><svg width="12" height="12" viewBox="0 0 12 12"><rect width="12" height="12" rx="1.5" fill="#fff"/><rect x="2" y="6" width="2" height="4" fill="#1f6bff"/><rect x="5" y="3" width="2" height="7" fill="#1f6bff"/><rect x="8" y="5" width="2" height="5" fill="#1f6bff"/></svg></div><h3>Real-Time Reports</h3><p>View your earnings, trade history, and rebate breakdown live inside your dashboard.</p></div>
      <div class="why-card"><div class="ico"><svg width="12" height="12" viewBox="0 0 12 12"><path d="M2 1h8v3a4 4 0 01-8 0z" fill="#ffc23d"/><rect x="5" y="7" width="2" height="3" fill="#ffc23d"/><rect x="3" y="10" width="6" height="1.5" fill="#ffc23d"/></svg></div><h3>Highest Rebate Rates</h3><p>We negotiate exclusively to ensure you receive the maximum possible rebate from every broker.</p></div>
      <div class="why-card"><div class="ico"><svg width="10" height="12" viewBox="0 0 12 14"><path d="M7 0L1 8h4l-1 6 6-8H6z" fill="#ffc23d"/></svg></div><h3>Daily Fast Payouts</h3><p>Receive your rebates daily via USDT, Bitcoin, bank transfer, Payvault, and more.</p></div>
      <div class="why-card"><div class="ico"><svg width="12" height="12" viewBox="0 0 12 12"><path d="M6 1C3 1 1 3 1 5.5c0 1.4.7 2.6 1.8 3.4L2.5 11l2.6-1.2c.3.1.6.1.9.1 3 0 5-2 5-4.5S9 1 6 1z" fill="#fff"/></svg></div><h3>Dedicated Support</h3><p>Our expert team responds within minutes on Chatline, live chat, or email — 24/5.</p></div>
    </div>
  </div>
</section>

<section class="steps">
  <div class="band"></div>
  <div class="wrap inner center">
    <div class="eyebrow">Get Started</div>
    <h2 class="sec-title" style="font-size:21px">Earn Forex Cashback in 3 Easy Steps</h2>
    <p class="sec-lead">Join TRADEBACKS, trade with partner brokers, and get paid automatically.</p>
    <div class="step-grid" style="text-align:left">
      <div class="step"><span class="num">1</span><div class="ico"><svg width="13" height="13" viewBox="0 0 12 12"><circle cx="6" cy="4" r="2.5" fill="#fff"/><path d="M1.5 11a4.5 4 0 019 0z" fill="#fff"/></svg></div><h3>Create Your Account</h3><p>Sign up for free in under 2 minutes and activate your cashback profile. No deposit required to register.</p></div>
      <div class="step"><span class="num">2</span><div class="ico"><svg width="13" height="13" viewBox="0 0 12 12"><path d="M5 7l2-2M4.5 5.5L3 7a1.8 1.8 0 002.5 2.5L7 8M7.5 6.5L9 5a1.8 1.8 0 00-2.5-2.5L5 4" stroke="#fff" stroke-width="1.3" fill="none"/></svg></div><h3>Link Your Trading Account</h3><p>Open a new account or connect your existing trading account with any of our 40+ partner brokers.</p></div>
      <div class="step"><span class="num">3</span><div class="ico"><svg width="13" height="13" viewBox="0 0 12 12"><rect x="1" y="3" width="10" height="6" rx="1" fill="#5fd38a"/><circle cx="6" cy="6" r="1.6" fill="#2d8f56"/></svg></div><h3>Receive Cashback Daily</h3><p>Earn automatic rebate payments on every eligible trade. Withdraw instantly to your preferred method.</p></div>
    </div>
  </div>
</section>

<section class="proof">
  <div class="wrap inner" style="height:638px">
    <div class="eyebrow">Trust &amp; Social Proof</div>
    <h2 class="sec-title">Real Traders. Real Payouts.</h2>
    <p class="sec-lead">Every screenshot below is a genuine payment received by our traders. No stock photos. No fake numbers.</p>

    <div class="quotes">
      <div class="quote">
        <div class="who"><span class="avatar" style="background:#4a5fe0">B</span><div><b>Bayu Pratama</b><small>Trading with Northgate FX</small></div></div>
        <div class="stars">★★★★★</div>
        <p>I've been using TRADEBACKS for 8 months now. The daily payouts are always on time and the rates are genuinely the best I've found. My spreads haven't changed at all.</p>
        <span class="earned">💰 Earned $3,240 total</span>
      </div>
      <div class="quote">
        <div class="who"><span class="avatar" style="background:#1fa57a">K</span><div><b>Kwame Mensah</b><small>Trading with Exvora</small></div></div>
        <div class="stars">★★★★★</div>
        <p>Finally a rebate service that actually pays. Setup took less than 10 minutes. I'm now getting $400–600 back every month just from my normal trading volume.</p>
        <span class="earned">💰 Earned $5,120 total</span>
      </div>
      <div class="quote">
        <div class="who"><span class="avatar" style="background:var(--orange)">A</span><div><b>Anan Wongsa</b><small>Trading with Peakline</small></div></div>
        <div class="stars">★★★★★</div>
        <p>Very transparent platform. You can see every lot counted in real time. The Chatline support team helped me link my account in minutes. Highly recommended.</p>
        <span class="earned">💰 Earned $2,780 total</span>
      </div>
    </div>

    <div class="payouts">
      <div class="pay-head">Verified Payouts <span>Recently Paid</span></div>
      <div class="pay-grid">
        <div class="pay"><small>USDT Transfer</small><span class="new">NEW</span><b>$412.30</b><em>Jun 15, 2026</em></div>
        <div class="pay"><small>Bank Transfer</small><span class="new">NEW</span><b>$891.00</b><em>Jun 11, 2026</em></div>
        <div class="pay"><small>Bitcoin</small><b>$245.80</b><em>Jun 10, 2026</em></div>
        <div class="pay"><small>Payvault</small><b>$1,200.00</b><em>Jun 08, 2026</em></div>
      </div>
      <div class="methods">WITHDRAWAL METHODS</div>
      <div class="chips"><span>₮ USDT</span><span>₿ Bitcoin</span><span>Ξ Ethereum</span><span>Payvault</span><span>Bank</span></div>
    </div>
  </div>
</section>

<section class="faq">
  <div class="wrap inner center">
    <div class="eyebrow">FAQ</div>
    <h2 class="sec-title" style="font-size:21px">Common Questions</h2>
    <div class="faq-list" style="text-align:left">
      <div class="faq-open">
        <div class="faq-q">What is a Forex Rebate? <span>+</span></div>
        <p>A forex rebate is a portion of the spread or commission you pay on each trade, returned to you as cashback. Since brokers pay introducers a commission for bringing clients, TRADEBACKS simply shares that commission back with you — every trade, automatically.</p>
      </div>
      <div class="faq-q">Does it affect my trading conditions? <span>+</span></div>
      <div class="faq-q">When are rebates paid? <span>+</span></div>
      <div class="faq-q">Can I link an existing broker account? <span>+</span></div>
      <div class="faq-q" style="border:none">How do I withdraw my earnings? <span>+</span></div>
    </div>
  </div>
</section>

<section class="cta">
  <div class="band"></div>
  <div class="wrap inner center">
    <h2>Start Earning Forex<br>Rebates Today</h2>
    <p>Join 15,000+ traders already receiving cashback from every trade they place.</p>
    <div class="cta-btns"><span class="btn btn-primary">Create Free Account</span><span class="btn btn-ghost">Compare Brokers</span></div>
  </div>
</section>

<footer class="footer">
  <div class="wrap inner">
    <div class="f-brand">
      <div class="logo"><span class="logo-dot"></span>TRADEBACKS</div>
      <p>The premium forex rebate platform trusted by 15,000+ traders globally. Earn cashback from every trade you place.</p>
      <div class="socials" role="img" aria-label="Social network links"><i></i><i></i><i></i><i></i></div>
    </div>
    <div class="f-col"><h4>COMPANY</h4><a>About Us</a><a>Contact</a><a>News</a></div>
    <div class="f-col"><h4>RESOURCES</h4><a>Brokers</a><a>Calculator</a><a>FAQ</a></div>
    <div class="f-col"><h4>LEGAL</h4><a>Privacy Policy</a><a>Terms &amp; Conditions</a></div>
    <div class="f-bottom">
      <span>© 2026 Tradebacks.com · All rights reserved</span>
      <span class="disc">Risk Disclaimer: Trading forex carries a high level of risk and may not be suitable for all investors. Past performance is not indicative of future results. Tradebacks.com is an independent rebate provider and does not provide investment advice.</span>
    </div>
  </div>
</footer>

</body>
</html>
```